Web Design for Small Healthcare Startup

Hello,

We are seeking a Website Design for a healthcare company focusing on mobile vaccinations, employee health and wellness services onsite at businesses, and consulting services relating to Healthcare Entities in WA state. Our company’s mission is to “To aid in a healthier workplace”. Brightpath Rovers will provide on-site wellness services to employers that simplify and streamline employee preventative health as well as onsite consulting services to help with compliance of Healthcare Entities.

We are seeking a Website Design for Brightpath Rovers, PLLC. Our company’s mission is to provide mobile health and wellness services to employers onsite at their businesses. These services include mobile vaccinations clinics for employees as well as wellness and health screenings. The company will also offer healtcare compliance consulting services for Healthcare Entities. The company was founded to bring these important healthcare services to businesses and keep employees healthy. Healthy employees are the cornerstone to a great business and we want to help orginazations achieve their goals of having a healthy productive workforce.

We are looking for a moderin website design that will need to be coded. We have attached our current logo design for reference as well as a brief questionare regarding our business for your information (not necessary to include all information). We would like something SEO friendly and easy to navigate.

Thank you!

Brightpath Rovers, PLLC

Target Market(s)

Small Businesses

Industry/Entity Type

Healthcare

Coding

Coded - Design and coding required

Number of Pages Required

1 page

Requirements
Nice to have
• SEO Friendly, Incorporate Logo

```html
<!DOCTYPE html>
<html lang="en">
<head>
<meta charset="utf-8">
<title>Brightpath Rovers, PLLC – Making the workplace a healthier place</title>
<meta name="description" content="Brightpath Rovers provides on-site mobile vaccine clinics and employee wellness services for businesses in Washington state.">
<link rel="stylesheet" href="https://fonts.googleapis.com/css2?family=Poppins:wght@400;500;600;700&display=swap">
<style>
:root{
  --blue:#1b5fc9;
  --blue-dark:#0d47a8;
  --blue-light:#8cb8f0;
  --pink:#c24fc4;
  --purple:#ac2fbd;
  --ink:#3a3340;
  --text:#2b2b2b;
  --muted:#9a9a9a;
  --lavender:#ecebfb;
  --line:#7a7a7a;
}
*{box-sizing:border-box;margin:0;padding:0}
html,body{width:1200px;height:3741px;overflow:hidden}
body{font-family:'Poppins',sans-serif;color:var(--text);background:#fff;position:relative}
section,header,nav,footer{position:absolute;left:0;width:1200px}
.abs{position:absolute}
a{color:inherit;text-decoration:none}

/* top bar */
.topbar{top:0;height:29px;background:var(--blue);color:#fff;font-size:10px}
.topbar .contact{top:8px;display:flex;align-items:center;gap:6px;white-space:nowrap}
.topbar .social{right:108px;top:7px;display:flex;gap:9px}
.topbar .social span{width:15px;height:15px;border-radius:50%;background:#fff;display:block}

/* nav */
.nav{top:29px;height:61px;background:#fff}
.brand{font-weight:600;color:var(--blue);font-size:12px;display:flex;align-items:center;gap:5px;white-space:nowrap}
.brand i{width:10px;height:10px;border-radius:50%;background:var(--pink);display:block}
.nav .brand{left:110px;top:22px}
.nav ul{list-style:none;left:655px;top:23px;display:flex;font-size:11px;color:#333;white-space:nowrap}
.nav li{margin-right:30px}
.btn{display:inline-flex;align-items:center;justify-content:center;border-radius:5px;font-size:11px;font-weight:500}
.btn-pink{background:var(--pink);color:#fff}
.nav .btn{left:976px;top:16px;width:116px;height:29px}

/* hero */
.hero{top:90px;height:510px;background:linear-gradient(100deg,#fff 40%,#ece6fb 100%)}
.eyebrow{left:107px;top:92px;font-size:12px;color:var(--blue);display:flex;align-items:center;gap:8px}
.eyebrow::after{content:"";width:45px;height:1.5px;background:var(--blue)}
.hero h1{left:107px;top:118px;font-size:51px;line-height:60px;font-weight:600;color:var(--ink);white-space:nowrap}
.hero h1 em{font-style:normal;color:var(--pink)}
.hero p{left:107px;top:254px;width:450px;font-size:12.5px;line-height:18px;color:var(--muted)}
.hero .btn{top:355px;height:29px}
.btn-outline{border:1.5px solid #333;background:#fff;color:#222}
.hero-photo{left:780px;top:128px;width:312px;height:331px;border-radius:36px 36px 90px 36px;background:linear-gradient(160deg,#7fb2ee,#2d6fd2)}

/* different */
.different{top:600px;height:552px}
.blob{background:linear-gradient(150deg,#7fb0ee,#1c5ec4);border-radius:48% 52% 45% 55%/40% 45% 55% 60%}
.different .blob{left:109px;top:95px;width:450px;height:398px}
.h2{font-size:37px;font-weight:600;color:#222;white-space:nowrap}
.different .h2{left:612px;top:100px}
.points{left:612px;top:176px;width:480px;list-style:none}
.points li{display:flex;gap:16px;font-size:12px;line-height:20px;height:54px}
.points b{flex:0 0 29px;height:29px;background:var(--blue);color:#fff;font-weight:500;font-size:14px;display:flex;align-items:center;justify-content:center;border-radius:3px}
.points span{padding-top:4px}

/* stats */
.stats{top:1152px;height:188px;background:var(--lavender)}
.stat{width:240px;text-align:center;top:30px}
.stat .icon{width:92px;height:92px;margin:0 auto;border-radius:50%;background:#fff;display:flex;align-items:center;justify-content:center}
.stat p{margin-top:20px;font-size:15px;font-weight:500;color:#222;white-space:nowrap}

/* about */
.about{top:1340px;height:546px}
.about .h2{left:107px;top:85px}
.about .copy{left:107px;top:150px;width:485px;font-size:12px;line-height:21px}
.about .copy p{margin-bottom:6px}
.about .btn{left:107px;top:416px;width:111px;height:29px}
.about-photo{left:615px;top:59px;width:399px;height:410px;border-radius:50%;background:linear-gradient(150deg,#5c79a8,#d8d0c8)}

/* services */
.services{top:1886px;height:494px;background:linear-gradient(160deg,#a8cbf8 0%,#3f7fdc 45%,#0d4aa8 100%);color:#fff}
.services .white-blob{left:113px;top:29px;width:451px;height:446px;background:#fff;border-radius:52% 48% 40% 60%/45% 50% 50% 55%}
.services .staff{left:170px;top:10px;width:300px;height:446px;background:linear-gradient(180deg,#d9c2b6,#243a66);border-radius:40% 40% 10% 10%}
.services .h2{left:612px;top:28px;color:#fff}
.services .copy{left:612px;top:90px;width:480px;font-size:10.8px;line-height:18px;text-transform:uppercase}
.services .copy p{margin-bottom:12px}
.services .btn{left:612px;top:414px;width:178px;height:29px;background:#fff;color:var(--blue)}

/* pricing */
.pricing{top:2380px;height:395px}
.center{left:0;width:1200px;text-align:center}
.pricing .h2{top:60px}
.card{top:148px;width:313px;height:218px;background:#fff;box-shadow:0 4px 16px rgba(0,0,0,.09);border-radius:4px;padding:20px 23px}
.card h3{font-size:38px;font-weight:600;color:var(--purple);line-height:50px}
.card p{margin-top:10px;font-size:12.5px;line-height:20px}
.card .btn{margin-top:27px;width:268px;height:53px;border-radius:10px;font-size:18px;font-weight:600}

/* inquiry */
.inquiry{top:2775px;height:622px}
.inquiry .h2{top:34px}
.form label{display:block;font-size:15px;font-weight:500;color:#111;line-height:18px}
.form .field{left:109px;width:413px}
.form .box{width:413px;border:1px solid #777;background:#fff;font-size:14px;color:#555;padding:0 14px;display:flex;align-items:center}
.form .btn{left:109px;top:508px;width:100px;height:29px}
.inquiry .blob{left:642px;top:116px;width:450px;height:447px}

/* footer */
.footer{top:3397px;height:344px;background:var(--lavender);font-size:10.5px}
.footer .brand{left:123px;top:50px;font-size:13px}
.footer .tag{left:106px;top:108px}
.footer .line{left:106px;display:flex;align-items:center;gap:8px;white-space:nowrap}
.col{top:42px}
.col h4{font-size:13px;font-weight:500;color:#111;margin-bottom:14px;white-space:nowrap}
.col li{list-style:none;line-height:27px;white-space:nowrap}
.news{left:824px;top:72px;display:flex}
.news .in{width:193px;height:37px;border:1px solid #8aa;background:#fff;color:#999;display:flex;align-items:center;padding-left:18px}
.news .go{width:75px;height:37px;background:var(--blue-dark);color:#fff;display:flex;align-items:center;justify-content:center}
.fsocial{left:824px;top:132px;display:flex;gap:25px}
.fsocial span{width:22px;height:22px;border-radius:50%;background:var(--blue-dark);display:block}
.footer .rule{left:107px;top:295px;width:985px;height:1px;background:#555}
.footer .rights{top:313px;font-size:10.5px}
</style>
</head>
<body>

<header class="topbar">
  <div class="abs contact" style="left:108px">
    <svg width="11" height="11" viewBox="0 0 24 24" fill="#fff"><path d="M6.6 10.8a15.1 15.1 0 006.6 6.6l2.2-2.2c.3-.3.7-.4 1-.2 1.1.4 2.3.6 3.6.6.6 0 1 .4 1 1V20c0 .6-.4 1-1 1A17 17 0 013 4c0-.6.4-1 1-1h3.5c.6 0 1 .4 1 1 0 1.3.2 2.5.6 3.6.1.3 0 .7-.2 1z"/></svg>
    +1 555 014 2290
  </div>
  <div class="abs contact" style="left:222px">
    <svg width="12" height="10" viewBox="0 0 24 18"><path d="M1 1h22v16H1z" fill="none" stroke="#fff" stroke-width="2"/><path d="M1 1l11 9 11-9" fill="none" stroke="#fff" stroke-width="2"/></svg>
    hello@brightpathrovers.example
  </div>
  <div class="abs social"><span></span><span></span><span></span></div>
</header>

<nav class="nav">
  <a class="abs brand" href="#"><i></i>Brightpath Rovers</a>
  <ul class="abs">
    <li>HOME</li><li>OUR &nbsp;SERVICES</li><li>ABOUT</li><li>PRICING</li>
  </ul>
  <a class="abs btn btn-pink" href="#">SCHEDULE</a>
</nav>

<section class="hero">
  <div class="abs eyebrow">Brightpath Rovers, PLLC</div>
  <h1 class="abs">Making the workplace<br>a <em>healthier</em> place</h1>
  <p class="abs">Brightpath Rovers specializes in providing seamless, hassle-free, on-site mobile vaccine clinics. Great service to offer as part of your company's Employee Wellness Package.</p>
  <a class="abs btn btn-pink" href="#" style="left:106px;width:115px">Book Now</a>
  <a class="abs btn btn-outline" href="#" style="left:237px;width:126px">Hlep Center</a>
  <div class="abs hero-photo" role="img" aria-label="Smiling doctor in a white coat holding a syringe"></div>
</section>

<section class="different">
  <div class="abs blob" role="img" aria-label="Doctor in a white coat with a stethoscope, arms crossed"></div>
  <h2 class="abs h2">What Make Us Different</h2>
  <ol class="abs points">
    <li><b>1</b><span>No crowded waiting rooms, no long lines, no hassle!</span></li>
    <li><b>2</b><span>Specializing in workplace employee vaccine clinics. Great service to offer as part of your company's Employee Wellness Package.</span></li>
    <li><b>3</b><span>Offering Flu and Covid vaccinations</span></li>
    <li><b>4</b><span>Brightpath Rovers specializes in providing seamless, hassle-free, on-site mobile vaccine clinics.</span></li>
  </ol>
</section>

<section class="stats">
  <div class="abs stat" style="left:53px">
    <div class="icon"><svg width="50" height="50" viewBox="0 0 50 50" fill="var(--pink)"><circle cx="25" cy="14" r="9"/><path d="M7 46c0-12 8-20 18-20s18 8 18 20z"/></svg></div>
    <p>2000+ Specialist</p>
  </div>
  <div class="abs stat" style="left:358px">
    <div class="icon"><svg width="50" height="50" viewBox="0 0 50 50" fill="none" stroke="var(--pink)" stroke-width="5" stroke-linecap="round"><path d="M10 40L34 16M28 10l12 12M38 6l6 6M10 40l-4 4"/></svg></div>
    <p>50000+ Vaccine Delivered</p>
  </div>
  <div class="abs stat" style="left:651px">
    <div class="icon"><svg width="50" height="50" viewBox="0 0 50 50" fill="var(--pink)"><path d="M25 4L3 22h6v24h32V22h6z"/><path d="M22 20h6v6h6v6h-6v6h-6v-6h-6v-6h6z" fill="#fff"/></svg></div>
    <p>50+ CLINICS</p>
  </div>
  <div class="abs stat" style="left:910px">
    <div class="icon"><svg width="50" height="50" viewBox="0 0 50 50" fill="var(--pink)"><rect x="4" y="8" width="42" height="38" rx="4"/><g fill="#fff"><rect x="10" y="20" width="8" height="8"/><rect x="21" y="20" width="8" height="8"/><rect x="32" y="20" width="8" height="8"/><rect x="10" y="32" width="8" height="8"/><rect x="21" y="32" width="8" height="8"/><rect x="32" y="32" width="8" height="8"/></g></svg></div>
    <p>2 SPET BOOKING</p>
  </div>
</section>

<section class="about">
  <h2 class="abs h2">About Us</h2>
  <div class="abs copy">
    <p>Brightpath Rovers, PLLC mission: Making the workplace a healthier place.</p>
    <p>To provide on-site wellness services to employers that simplify and streamline employee preventative health.</p>
    <p>Pharmacist owned and operated.</p>
    <p>Brightpath Rovers, PLLC was started by local, Washington state licensed pharmacist with over 15 years experience vaccinating patients. She is a highly skilled immunizer and enjoys interacting with patients while providing this important preventative health services. Her vaccination experience spans from individual patient vaccinations to large clinics during community outbreaks.</p>
  </div>
  <a class="abs btn btn-pink" href="#">About Us</a>
  <div class="abs about-photo" role="img" aria-label="Pharmacist giving a patient a vaccination in the arm, with vaccine vials"></div>
</section>

<section class="services">
  <div class="abs white-blob"></div>
  <div class="abs staff" role="img" aria-label="Smiling nurse in navy scrubs with a stethoscope"></div>
  <h2 class="abs h2">Our Services</h2>
  <div class="abs copy">
    <p>Brightpath Rovers will come to you!</p>
    <p>No crowded waiting rooms, no long lines, no hassle!</p>
    <p>Hassle-free, streamlining the vaccination process … provide this on-site service as part of your employee wellness package</p>
    <p>Serving employers who want to increase the health and wellness of their workplace &nbsp;vaccines including seasonal flu, covid, pneumonia</p>
    <p>Ensure your employees and their families remain healthy this flu season. Host a flu shot clinic on site to help your employees get vaccinated. Provide this service as part of your employee wellness benefits package.</p>
    <p>Don't wait for your employees to get their vaccines at their next doctor's appointment or visit to the pharmacy. Provide this desired employee benefit on site with no crowded waiting rooms, no long lines, no hassle!</p>
  </div>
  <a class="abs btn" href="#">View All Services</a>
</section>

<section class="pricing">
  <h2 class="abs h2 center">A Pricing Plan For Every Enterprise</h2>
  <div class="abs card" style="left:107px"><h3>Essential</h3><p>Ideal for organizers have<br>5-20 employees</p><a class="btn btn-pink" href="#">Request A Quote</a></div>
  <div class="abs card" style="left:443px"><h3>Medium</h3><p>Ideal for organizers have<br>20-100 employees</p><a class="btn btn-pink" href="#">Request A Quote</a></div>
  <div class="abs card" style="left:779px"><h3>Large</h3><p>Ideal for organizers have<br>100-500 employees</p><a class="btn btn-pink" href="#">Request A Quote</a></div>
</section>

<section class="inquiry">
  <h2 class="abs h2 center">Quick Inquiry</h2>
  <form class="form">
    <div class="abs field" style="top:158px"><label>Name</label><div class="box" style="height:44px;margin-top:2px">John</div></div>
    <div class="abs field" style="top:234px"><label>Email</label><div class="box" style="height:44px;margin-top:2px">example@xyz.com</div></div>
    <div class="abs field" style="top:310px"><label>Subject</label><div class="box" style="height:44px;margin-top:2px"></div></div>
    <div class="abs field" style="top:385px"><label>Massage</label><div class="box" style="height:83px;margin-top:2px"></div></div>
    <a class="abs btn btn-pink" href="#">Submit</a>
  </form>
  <div class="abs blob" role="img" aria-label="Smiling nurse in blue scrubs giving two thumbs up"></div>
</section>

<footer class="footer">
  <div class="abs brand"><i></i>Brightpath Rovers</div>
  <p class="abs tag">Making the workplace a healthier place.</p>
  <p class="abs line" style="top:136px"><svg width="10" height="10" viewBox="0 0 24 24" fill="#333"><path d="M6.6 10.8a15.1 15.1 0 006.6 6.6l2.2-2.2c.3-.3.7-.4 1-.2 1.1.4 2.3.6 3.6.6.6 0 1 .4 1 1V20c0 .6-.4 1-1 1A17 17 0 013 4c0-.6.4-1 1-1h3.5c.6 0 1 .4 1 1 0 1.3.2 2.5.6 3.6.1.3 0 .7-.2 1z"/></svg>+1 555 014 2290</p>
  <p class="abs line" style="top:162px"><svg width="11" height="9" viewBox="0 0 24 18"><path d="M1 1h22v16H1z" fill="none" stroke="#333" stroke-width="2"/><path d="M1 1l11 9 11-9" fill="none" stroke="#333" stroke-width="2"/></svg>hello@brightpathrovers.example</p>
  <div class="abs col" style="left:362px"><h4>Quick Link</h4><ul><li>Home</li><li>About</li><li>Our &nbsp;Services</li><li>Pricing</li></ul></div>
  <div class="abs col" style="left:498px"><h4>OUR STORY</h4><ul><li>Who We Are</li><li>Historic Timeline</li><li>Careers</li><li>Press &amp; Media</li></ul></div>
  <div class="abs col" style="left:644px"><h4>WORK WITH US</h4><ul><li>Partners</li><li>Careers</li><li>Local Comunity</li><li>Living Landscape</li></ul></div>
  <div class="abs col" style="left:824px"><h4>Subscribe To Our Newsletter</h4></div>
  <div class="abs news"><div class="in">Email Address</div><div class="go">Submit</div></div>
  <div class="abs fsocial"><span></span><span></span><span></span></div>
  <div class="abs rule"></div>
  <p class="abs rights center">© 2022 All rights reserved by BrightpathRovers</p>
</footer>

</body>
</html>
```